Corporate Identity for our Company

For this project we need to explain a few things:
We started off in 1933 as a food processing company with main business of Edible oil sold as T Seal. The main colour were red, black and white but those were simple times. The design became immensely popular because of good product and great marketing. Later on We used a lot of yellow as well on the background for our product designs, wall painting etc and also the label. So the colours of our company became RED, YELLOW, BLACK & WHITE. Please check the website for reference http://zenwaygrainworks.com/edible-oils.php
The family business divided into two parts in 1995. We got T seal for items agonised in class 30 of Indian trademark act & our cousins for class 29. We have since only focused on wheat products and are now looking at capitalising our benefits for other products in class 30 which are food items like Besan, Lentils, salt, spices etc. ( for a complete list please visit http://www.quiblex.com/legal-encyclopedia/trademark-class-30-coffee-flour-rice-products.html)
We have also made a website please check : http://vantelhubdock.net/~tseal/
Username : rovelpage
Password : wendrix@Glade72
You can help by redesigning our stationery, letter pads etc. so we can maintain consistency that enables customer recall/ recognition for our company's profile.
I'm attaching pictures of our current stationary (letter pads) and pictures of our products. This will help you get an idea about our company's current design patterns.
Letter pad:
Dimensions/Size: A4
colours: Any
Information to be added:
Admin. office: 7 B/D Stock Shed,
Jammu (J&K)
Ph. no.: 0191-2867403 ; Fax: 0191-2867459
Units:
Sona Kiran Flour Mills
New Sona Kiran Flour Mills
Lane No. 9
TEMBRA Industrial Complex,
Bari Brahmana, Jammu (J&K)
Ph no. 0192-3584076
Email: support@tsealgoods.com
1) Business cards:
Dimensions: L x B (3.5" x 2 ") printable size
Colours: multi colour
Information:
should contain the T seal logo,
Name of the person
company Address (which you have already)
ph no (we will fill that in)
and email. (we will fill that in)
2) Envelopes:
Dimensions:
L x B (14" x 12")
Colour: Multi
information: T seal logo
contact information and address

```html
<!DOCTYPE html>
<html lang="en">
<head>
<meta charset="utf-8">
<title>T Seal Stationery</title>
<link href="https://fonts.googleapis.com/css2?family=Roboto+Condensed:wght@400;700&display=swap" rel="stylesheet">
<style>
:root{
  --red:#ad1119;
  --yellow:#f7c21b;
  --white:#ffffff;
  --ink:#1a1a1a;
  --grey:#6b6b6b;
  --glow-strong:rgba(236,84,30,.85);
  --glow-mid:rgba(245,140,70,.45);
  --glow-none:rgba(255,220,190,0);
}
*{margin:0;padding:0;box-sizing:border-box}
html,body{width:1200px;height:787px;overflow:hidden}
body{background:linear-gradient(180deg,#d0d2d4,#b9bbbe);font-family:"Roboto Condensed",Arial,sans-serif;position:relative;color:var(--ink)}
.sheet{position:absolute;background:var(--white);box-shadow:0 6px 14px rgba(0,0,0,.25);overflow:hidden}
.abs{position:absolute}
.glow{position:absolute;left:0;width:100%}
.glow-top{top:0;background:linear-gradient(180deg,var(--glow-strong) 0%,var(--glow-mid) 45%,var(--glow-none) 100%)}
.glow-bottom{bottom:0;background:linear-gradient(0deg,var(--glow-strong) 0%,var(--glow-mid) 45%,var(--glow-none) 100%)}
.label{position:absolute;font-weight:700;font-size:17px;letter-spacing:.2px;color:var(--ink);transform:translateX(-50%);white-space:nowrap}
.seal{position:absolute;border-radius:50%;background:var(--yellow);border:3px solid var(--red);display:flex;align-items:center;justify-content:center;color:var(--red);font-weight:700;white-space:nowrap}
.band{position:absolute;left:0;width:100%;background:var(--red)}
.line{position:absolute;white-space:nowrap;line-height:1}
.co{color:var(--yellow);font-weight:700}
.hi{color:var(--yellow)}
.b{font-weight:700}
.rd{color:var(--red);font-weight:700}
/* letterhead */
.letterhead{left:60px;top:88px;width:386px;height:545px}
.letterhead .band{top:0;height:64px}
.letterhead .seal{left:46px;top:24px;width:80px;height:80px;font-size:17px}
.letterhead .line{left:138px}
.letterhead .glow-bottom{height:85px}
/* business cards */
.card{top:27px;width:164px;height:93px}
.card-front{left:646px;background:var(--red)}
.card-front .seal{left:57px;top:18px;width:50px;height:50px;font-size:11px;border-color:var(--yellow)}
.card-back{left:826px}
.card-back .glow-top{height:28px}
.card-back .seal{left:12px;top:22px;width:44px;height:44px;font-size:10px}
.card-back .divider{left:62px;top:30px;width:1px;height:48px;background:#cccccc}
/* envelope */
.envelope{left:508px;top:169px;width:653px;height:558px}
.envelope .glow-top{height:115px}
.envelope .band{top:494px;height:64px}
.envelope .seal{left:65px;top:420px;width:110px;height:110px;font-size:24px;border-width:4px;z-index:2}
.envelope .line{left:199px;font-size:8.6px}
</style>
</head>
<body>

<!-- Letterhead -->
<section class="sheet letterhead" aria-label="Letterhead">
  <div class="band"></div>
  <div class="seal">T Seal</div>
  <p class="line co" style="top:41px;font-size:9px">KRV FOODS PVT. LTD.</p>
  <p class="line" style="top:52px;font-size:5.8px;color:#fff"><span class="b">Admin. office:</span> 7 B/D Stock Shed, <span class="b">Jammu (J&amp;K)</span></p>
  <p class="line" style="top:59px;font-size:5.8px;color:#fff"><span class="b">Ph. no.:</span> 0191-2867403 - <span class="b">Fax:</span> 0191-2867459</p>
  <p class="line" style="top:70px;font-size:5.8px;color:var(--grey)"><span class="b">Units: Sona Kiran Flour Mills - New Sona Kiran Flour Mills</span></p>
  <p class="line" style="top:78px;font-size:5.8px;color:var(--grey)">Lane No. 9, TEMBRA Industrial Complex, Bari Brahmana, Jammu (J&amp;K) - 18 1140</p>
  <p class="line" style="top:86px;font-size:5.8px;color:var(--grey)"><span class="rd">Ph no.</span> 0192-3584076 - <span class="rd">Email:</span> support@tsealgoods.com</p>
  <div class="glow glow-bottom" role="img" aria-label="Decorative flowing orange light band"></div>
</section>
<p class="label" style="left:227px;top:650px">LETTERHEAD</p>

<!-- Business cards -->
<section class="sheet card card-front" aria-label="Business card front">
  <div class="seal">T Seal</div>
</section>
<section class="sheet card card-back" aria-label="Business card back">
  <div class="glow glow-top" role="img" aria-label="Decorative flowing orange light band"></div>
  <div class="seal">T Seal</div>
  <p class="line rd" style="left:10px;top:74px;font-size:5.6px">KRV FOODS PVT. LTD.</p>
  <div class="abs divider"></div>
  <p class="line" style="left:69px;top:32px;font-size:7px">Rohan <span class="b">Mehra</span></p>
  <p class="line rd" style="left:69px;top:42px;font-size:5.2px">Managing director</p>
  <p class="line" style="left:69px;top:54px;font-size:4.6px;color:var(--grey)">Lane No. 9, Tembra Industrial Complex,</p>
  <p class="line" style="left:69px;top:60px;font-size:4.6px;color:var(--grey)">Bari Brahmana, Jammu, J &amp; K - 18 1140</p>
  <svg class="abs" style="left:69px;top:66px" width="5" height="5" viewBox="0 0 10 10"><path d="M2 1l2 2-1 2 2 2 2-1 2 2-2 2C4 9 1 6 0 3z" fill="var(--red)"/></svg>
  <p class="line" style="left:77px;top:66px;font-size:4.6px;color:var(--grey)">+91 - 947 3321 570</p>
  <svg class="abs" style="left:69px;top:72px" width="5" height="4" viewBox="0 0 10 8"><rect width="10" height="8" fill="var(--red)"/><path d="M0 0l5 4 5-4" stroke="#fff" fill="none"/></svg>
  <p class="line" style="left:77px;top:72px;font-size:4.6px;color:var(--grey)">krvmetals@mailbox.com</p>
</section>
<p class="label" style="left:813px;top:136px">BUSINESS CARD</p>

<!-- Envelope -->
<section class="sheet envelope" aria-label="Envelope">
  <div class="glow glow-top" role="img" aria-label="Decorative flowing orange light band"></div>
  <div class="band"></div>
  <div class="seal">T Seal</div>
  <p class="line rd" style="top:469px;font-size:11px">KRV FOODS PVT. LTD.</p>
  <p class="line" style="top:482px;color:var(--grey)"><span class="b">Admin. office:</span> 7 B/D Stock Shed, <span class="b">Jammu (J&amp;K) - Ph. no.:</span> 0191-2867403 - <span class="b">Fax:</span> 0191-2867459</p>
  <p class="line b" style="top:500px;color:#fff">Units: Sona Kiran Flour Mills - New Sona Kiran Flour Mills. &nbsp;Lane No. 9, TEMBRA Industrial Complex,</p>
  <p class="line b" style="top:511px;color:#fff">Bari Brahmana, Jammu (J&amp;K) - 18 1140 - <span class="hi">Ph no.</span> 0192-3584076 - <span class="hi">Email:</span> support@tsealgoods.com</p>
</section>
<p class="label" style="left:829px;top:748px">ENVELOP</p>

</body>
</html>
```